Complete redesign of site for leading equipment supplier and service company

Looking for a new website design to portray our offerings for customers. Bay & Gate is a distributor, installer and service provider for loading dock equipment and industrial doors. We are a factory authorized dealer for a number of top brand names and also provide service after the sale on our equipment as well as competitors equipment. We are also in the midst of developing a service program tied to a QR coding system that would need to be incorporated in the website where a customer can scan a QR code and be brought to a specific "Service Request" portal that would be a form they could fill out to send to our service department.
Site should also feature product information pages for our base of product offerings, a completed projects area where we can showcase the work we've done, and a bio area for our sales and management team.

Some information for research:

Our Products That We Sell:

morrowliftworks.com
pallanraisetech.com
vqxgates.com
nhlsupplies.com
https://www.garvin-holtby.com/commercial-doors
https://www.pelmagates.com/
https://www.ulogates.com/

Similar Companies and Competitors:

http://www.quaddelmachinery.com/
https://www.easternbaysupplies.com/
https://www.moonmachinery.com/
https://www.ravenhollis.com/
https://pelvo.quandrift.com/en/us?gclid=ZqmPLRtyuv5XNCCFkpOmQD_ZYKJT0sVUr8PWHnm3K7Pxa3ZQ-PxluzkMnb-opiIIDmRtxu4BzJpTfLh9rmzDGbnwQ_ExcEB

Target Market(s)

Existing and potential customers throughout the greater New England region including:
Manufacturing
Distribution
Cold Storage
Pharmaceutical
Food Production
Beverage Bottling
Warehousing

Coding

Coded - Design and coding required

Number of Pages Required

5+ page

Colors
9ccb3b
ecf7fb

Requirements
Must have
• Home Page
Product Page
Service Page
Contact Page
Separate page that will be directed to from a QR code that we will supply to specific customers

```html
<!DOCTYPE html>
<html lang="en">
<head>
<meta charset="utf-8">
<title>Bay &amp; Gate</title>
<link href="https://fonts.googleapis.com/css2?family=Lato:wght@400;700;900&display=swap" rel="stylesheet">
<style>
:root{
  --green:#8dc63f;
  --ice:#e8f3f9;
  --ink:#111;
  --text:#333;
  --white:#fff;
  --dark:#222;
  --page:#f9f9f9;
}
*{box-sizing:border-box;margin:0;padding:0}
html,body{width:1200px;height:4009px;overflow:hidden}
body{position:relative;background:var(--page);font-family:'Lato',sans-serif;color:var(--text)}
.abs{position:absolute}
.btn{position:absolute;background:var(--green);color:var(--white);font-size:14px;font-weight:700;text-transform:uppercase;display:flex;align-items:center;justify-content:center;letter-spacing:.3px}
.h2{position:absolute;left:0;width:1200px;text-align:center;font-size:28px;font-weight:700;color:var(--ink);text-transform:uppercase}
.para{font-size:15.5px;line-height:30px;color:var(--text)}
.photo{position:absolute}

.topbar{left:0;top:0;width:1200px;height:100px;background:var(--page)}
.navbar{left:0;top:100px;width:1200px;height:55px;background:var(--green)}
.brand{left:75px;top:23px;width:110px;height:122px;background:var(--dark);border:3px solid var(--ink);display:flex;flex-direction:column;align-items:center;justify-content:center;gap:8px;z-index:3}
.brand .mark{width:16px;height:16px;background:var(--green)}
.brand span{color:var(--white);font-size:18px;font-weight:700;text-align:center;line-height:1.1}
.phone{right:75px;top:30px;display:flex;align-items:center;gap:22px;font-size:26px;font-weight:700;color:var(--ink)}
.phone .ico{width:40px;height:40px;border:2px solid var(--green);display:flex;align-items:center;justify-content:center}
.nav{left:223px;top:100px;height:55px;display:flex;align-items:center;gap:33px}
.nav a{color:var(--white);font-size:13.5px;text-decoration:none;text-transform:uppercase}
.nav a.active{color:var(--ink);font-weight:700}
.request{left:945px;top:100px;width:180px;height:55px;background:#000;color:var(--white);font-size:14px;font-weight:700;display:flex;align-items:center;justify-content:center}

.hero{left:0;top:155px;width:1200px;height:536px;background:linear-gradient(100deg,#5e6364 0%,#8b8e8f 35%,#7a6f64 60%,#c07a2d 85%,#b46a26 100%)}
.hero-title{left:0;top:310px;width:1200px;text-align:center;font-size:58px;font-weight:900;color:var(--white)}
.hero-sub{left:0;top:380px;width:1200px;text-align:center;font-size:24px;font-weight:700;color:var(--white);line-height:34px}
.dots{left:562px;top:642px;display:flex;gap:11px}
.dots i{width:10px;height:10px;border-radius:50%;background:var(--white)}
.dots i:first-child{background:var(--ink)}

.svc-bg{left:0;top:1046px;width:1200px;height:494px;background:var(--ice)}
.badge{left:470px;top:1190px;width:206px;height:206px;border-radius:50%;background:var(--white);box-shadow:0 4px 14px rgba(0,0,0,.2);display:flex;align-items:center;justify-content:center}
.badge div{width:104px;height:112px;background:var(--dark);color:var(--white);font-weight:700;font-size:17px;display:flex;align-items:center;justify-content:center;text-align:center;line-height:1.15}

.card{position:absolute;width:242px;height:233px}
.card .img{height:182px}
.card .lbl{height:51px;background:var(--green);color:var(--white);font-size:18px;font-weight:700;display:flex;align-items:center;justify-content:center}

.band{position:absolute;left:0;width:1200px;height:413px}
.split-title{font-size:28px;font-weight:700;color:var(--ink);text-transform:uppercase}

.news-bg{left:0;top:3210px;width:1200px;height:428px;background:var(--ice)}
.news{position:absolute;top:3325px;width:330px;height:246px;background:var(--white);border:3px solid var(--green);padding:22px 16px}
.news .date{color:var(--green);font-size:14px;font-weight:700}
.news h3{font-size:15.5px;font-weight:700;color:var(--ink);line-height:24px;margin-top:18px}
.news p{font-size:13px;line-height:23px;margin-top:10px}
.news a{display:block;margin-top:16px;color:var(--green);font-size:13px;text-decoration:underline}

.footer{left:0;top:3638px;width:1200px;height:314px;background:var(--white)}
.fbrand{left:75px;top:3700px;width:75px;height:82px;background:var(--dark);border:2px solid var(--ink);color:var(--white);font-size:13px;font-weight:700;display:flex;align-items:center;justify-content:center;text-align:center;line-height:1.1}
.ftext{left:75px;top:3800px;width:280px;font-size:13px;line-height:23px}
.fh{font-size:16px;font-weight:700;color:var(--ink)}
.flist{font-size:13px;line-height:27.5px;list-style:none;margin-top:4px}
.crow{display:flex;align-items:center;gap:14px;font-size:13px;line-height:23px}
.crow svg{width:12px;height:12px}
.email{left:885px;top:3731px;width:240px;height:42px;border:1px solid #aaa;display:flex;align-items:center;gap:16px;padding-left:14px;font-size:13px}
.social{left:885px;top:3893px;display:flex;gap:18px}
.social i{width:20px;height:20px;border-radius:50%;background:#333;display:block}
.bottom{left:0;top:3952px;width:1200px;height:57px;background:var(--dark);color:var(--white);font-size:11px;display:flex;align-items:center;justify-content:center}
</style>
</head>
<body>

<header>
  <div class="abs topbar"></div>
  <div class="abs navbar"></div>
  <div class="abs brand"><div class="mark"></div><span>Bay &amp;<br>Gate</span></div>
  <div class="abs phone">
    <div class="ico"><svg width="20" height="20" viewBox="0 0 24 24"><path fill="#8dc63f" d="M6.6 10.8a15 15 0 0 0 6.6 6.6l2.2-2.2c.3-.3.7-.4 1-.2 1.1.4 2.3.6 3.6.6.6 0 1 .4 1 1V20c0 .6-.4 1-1 1A17 17 0 0 1 3 4c0-.6.4-1 1-1h3.5c.6 0 1 .4 1 1 0 1.3.2 2.5.6 3.6.1.3 0 .7-.2 1z"/></svg></div>
    1-800-555-0142
  </div>
  <nav class="abs nav">
    <a class="active">Home</a><a>About Us</a><a>Services</a><a>Products</a><a>Latest Project</a><a>Blog</a><a>Contact Us</a>
  </nav>
  <div class="abs request">SERVICE REQUEST</div>
</header>

<section>
  <div class="abs hero" role="img" aria-label="Loading dock with overhead doors and orange bollards"></div>
  <div class="abs hero-title">BAY &amp; GATE</div>
  <div class="abs hero-sub">Bay &amp; Gate is a distributor, installer and service provider for<br>loading dock equipment and industrial doors.</div>
  <div class="btn" style="left:525px;top:473px;width:149px;height:47px">Read More</div>
  <div class="abs dots"><i></i><i></i><i></i><i></i></div>
</section>

<section>
  <div class="h2" style="top:748px">Welcome to our website</div>
  <p class="abs para" style="left:0;top:802px;width:1200px;text-align:center">Lorem ipsum dolor sit amet, consectetur adipiscing elit. Nullam porttitor enim quis velit vestibulum, vel pretium velit mollis.<br>Aliquam pharetra ultrices erat et sollicitudin. Ut ac auctor metus. Praesent consectetur justo vehicula interdum vehicula.<br>Cras cursus id lorem in aliquet. Integer pharetra commodo consequat.</p>
  <div class="btn" style="left:525px;top:924px;width:151px;height:47px">Read More</div>
</section>

<section>
  <div class="abs svc-bg"></div>
  <svg class="abs" style="left:0;top:1046px" width="620" height="494" role="img" aria-label="Warehouse building with blue roller doors">
    <defs><linearGradient id="wh" x1="0" y1="0" x2="0" y2="1"><stop offset="0" stop-color="#7c8a99"/><stop offset=".55" stop-color="#2c56a6"/><stop offset="1" stop-color="#a9a49b"/></linearGradient></defs>
    <polygon points="0,0 618,0 529,494 0,494" fill="url(#wh)"/>
  </svg>
  <div class="abs badge"><div>Bay &amp;<br>Gate</div></div>
  <div class="abs split-title" style="left:703px;top:1134px">Our Services</div>
  <p class="abs para" style="left:705px;top:1184px;width:425px">Lorem ipsum dolor sit amet, consectetur adipiscing elit. Nullam porttitor enim quis velit vestibulum, vel pretium velit mollis. Aliquam pharetra ultrices erat et sollicitudin. Ut ac auctor metus. Praesent consectetur justo vehicula interdum vehicula. Cras cursus id lorem in aliquet. Integer pharetra commodo consequat.</p>
  <div class="btn" style="left:705px;top:1400px;width:151px;height:47px">Read More</div>
</section>

<section>
  <div class="h2" style="top:1594px">Featured Product</div>
  <div class="card" style="left:75px;top:1667px"><div class="img" role="img" aria-label="Orange industrial doors on dark building" style="background:linear-gradient(160deg,#3a3f4a,#c8501f)"></div><div class="lbl">Nullam porttitor</div></div>
  <div class="card" style="left:342px;top:1667px"><div class="img" role="img" aria-label="Scissor lift table" style="background:linear-gradient(160deg,#f2f2f2,#d6cdb8)"></div><div class="lbl">Nullam porttitor</div></div>
  <div class="card" style="left:616px;top:1667px"><div class="img" role="img" aria-label="Dock shelter with yellow door" style="background:linear-gradient(160deg,#9a9a96,#4a4a48 55%,#c9b23a)"></div><div class="lbl">Nullam porttitor</div></div>
  <div class="card" style="left:884px;top:1667px"><div class="img" role="img" aria-label="High-volume ceiling fan" style="background:linear-gradient(160deg,#6d7780,#2f3a45)"></div><div class="lbl">Nullam porttitor</div></div>
</section>

<section>
  <div class="band" style="top:1968px;background:var(--ice)"></div>
  <div class="photo" role="img" aria-label="Sales team reviewing charts at a desk" style="left:0;top:1968px;width:602px;height:413px;background:linear-gradient(120deg,#7d8f9c,#c9c6c0 45%,#b07a4c 80%,#3c4a5a)"></div>
  <div class="abs split-title" style="left:633px;top:2030px">Bio of Sales</div>
  <p class="abs para" style="left:633px;top:2084px;width:520px">Lorem ipsum dolor sit amet, consectetur adipiscing elit.<br>porttitor enim quis velit vestibulum, vel pretium velit mollis.<br>Aliquam pharetra ultrices erat et sollicitudin. Ut ac auctor metus.<br>Praesent consectetur justo vehicula interdum vehicula.<br>Cras cursus id lorem in aliquet.</p>
  <div class="btn" style="left:633px;top:2267px;width:153px;height:47px">Read More</div>

  <div class="band" style="top:2381px;background:var(--ice)"></div>
  <div class="abs split-title" style="left:75px;top:2443px">Management Team</div>
  <p class="abs para" style="left:75px;top:2497px;width:520px">Lorem ipsum dolor sit amet, consectetur adipiscing elit.<br>porttitor enim quis velit vestibulum, vel pretium velit mollis.<br>Aliquam pharetra ultrices erat et sollicitudin. Ut ac auctor metus.<br>Praesent consectetur justo vehicula interdum vehicula.<br>Cras cursus id lorem in aliquet.</p>
  <div class="btn" style="left:75px;top:2680px;width:152px;height:47px">Our Team</div>
  <div class="photo" role="img" aria-label="Team in hard hats and safety vests at a truck depot" style="left:602px;top:2381px;width:598px;height:412px;background:linear-gradient(110deg,#8e959c,#c9cdd1 40%,#b9c43a 65%,#b8353a 90%)"></div>
</section>

<section>
  <div class="h2" style="top:2840px">Latest Projects</div>
  <div class="card" style="left:75px;top:2911px"><div class="img" role="img" aria-label="Red dock doors with yellow guards" style="background:linear-gradient(160deg,#3a3e48,#a52a2a 60%,#8a8a86)"></div><div class="lbl">Nullam Porttitor</div></div>
  <div class="card" style="left:342px;top:2911px"><div class="img" role="img" aria-label="Grey dock with orange bumpers" style="background:linear-gradient(160deg,#8f9196,#5a5c60 55%,#e2782a)"></div><div class="lbl">Nullam Porttitor</div></div>
  <div class="card" style="left:616px;top:2911px"><div class="img" role="img" aria-label="Distribution center exterior under blue sky" style="background:linear-gradient(180deg,#3c7fd0,#e8eef4 50%,#9a8f8a)"></div><div class="lbl">Nullam Porttitor</div></div>
  <div class="card" style="left:884px;top:2911px"><div class="img" role="img" aria-label="Interior loading bays with red floor markings" style="background:linear-gradient(180deg,#e6e6e4,#c8c6c2 60%,#c33a36)"></div><div class="lbl">Nullam Porttitor</div></div>
</section>

<section>
  <div class="abs news-bg"></div>
  <div class="h2" style="top:3255px">News Updates</div>
  <article class="news" style="left:75px"><div class="date">Jun 30, 2020</div><h3>Aliquam molestie, mi et imperdiet euismod dui purus</h3><p>et interdum lacus lectus et accumsan sollicitudin sapien, sit amet adipiscing turpis gravida ac.</p><a>Read More</a></article>
  <article class="news" style="left:432px"><div class="date">Jun 30, 2020</div><h3>Aliquam molestie, mi et imperdiet euismod dui purus</h3><p>et interdum lacus lectus et accumsan sollicitudin sapien, sit amet adipiscing turpis gravida ac.</p><a>Read More</a></article>
  <article class="news" style="left:795px"><div class="date">Jun 30, 2020</div><h3>Aliquam molestie, mi et imperdiet euismod dui purus</h3><p>et interdum lacus lectus et accumsan sollicitudin sapien, sit amet adipiscing turpis gravida ac.</p><a>Read More</a></article>
</section>

<footer>
  <div class="abs footer"></div>
  <div class="abs fbrand">Bay &amp;<br>Gate</div>
  <p class="abs ftext">Aliquam molestie, mi et imperdiet euismod, dui purus auctor tellus, et interdum lacus lectus et ante. Sed accumsan sollicitudin sapien, sit amet adipiscing turpis gravida ac.</p>
  <div class="abs" style="left:437px;top:3698px">
    <div class="fh">Navigations</div>
    <ul class="flist"><li>Home</li><li>About Us</li><li>Services</li><li>Products</li><li>Latest Project</li><li>Blog</li><li>Contact Us</li></ul>
  </div>
  <div class="abs" style="left:630px;top:3698px">
    <div class="fh">Contact Info</div>
    <p style="font-size:13px;line-height:23px;margin-top:6px">4127 Harlow<br>Lane,Dunmere, D06 41KT</p>
    <div class="crow" style="margin-top:6px"><svg viewBox="0 0 24 24"><path fill="#333" d="M6.6 10.8a15 15 0 0 0 6.6 6.6l2.2-2.2c.3-.3.7-.4 1-.2 1.1.4 2.3.6 3.6.6.6 0 1 .4 1 1V20c0 .6-.4 1-1 1A17 17 0 0 1 3 4c0-.6.4-1 1-1h3.5c.6 0 1 .4 1 1 0 1.3.2 2.5.6 3.6.1.3 0 .7-.2 1z"/></svg>1-800-555-0142</div>
    <div class="crow"><svg viewBox="0 0 24 24"><path fill="#333" d="M2 5h20v14H2zM2 5l10 8 10-8" stroke="#fff" stroke-width="1.5"/></svg>info@bayandgate.com</div>
    <div class="crow"><svg viewBox="0 0 24 24"><path fill="#333" d="M12 2a7 7 0 0 0-7 7c0 5 7 13 7 13s7-8 7-13a7 7 0 0 0-7-7zm0 9.5a2.5 2.5 0 1 1 0-5 2.5 2.5 0 0 1 0 5z"/></svg>Map Location</div>
  </div>
  <div class="abs fh" style="left:885px;top:3698px">Email Subscribe</div>
  <div class="abs email"><svg width="14" height="12" viewBox="0 0 24 20"><path fill="#333" d="M0 0h24v20H0z"/><path d="M0 0l12 10L24 0" stroke="#fff" stroke-width="2" fill="none"/></svg>Email Address</div>
  <div class="btn" style="left:1032px;top:3786px;width:93px;height:36px;text-transform:none">Sign Up</div>
  <div class="abs fh" style="left:885px;top:3858px">Follow Us</div>
  <div class="abs social"><i aria-label="Social link"></i><i aria-label="Social link"></i><i aria-label="Social link"></i><i aria-label="Social link"></i><i aria-label="Social link"></i></div>
  <div class="abs bottom">Copyright © 2020. Company Name. All Right Reserved</div>
</footer>

</body>
</html>
```